Letterhead for Dorian Welk

I need a letterhead based on the business card design

Industry/Entity Type

Business

Requirements
Must have
• Footer: Dorian Welk Naturopath
Shop 4123c, 46 Carrow Lane, Sydney 2000

```html
<!DOCTYPE html>
<html lang="en">
<head>
<meta charset="utf-8">
<title>Dorian Welk Naturopath – Letterhead</title>
<link rel="stylesheet" href="https://fonts.googleapis.com/css2?family=Arimo:wght@400;700&display=swap">
<style>
  :root {
    --orange: #ee7623;
    --grey-text: #8a8a8a;
    --grey-light: #a8a8a8;
    --leaf-tone: #ececec;
    --paper: #ffffff;
    --edge: #9a9a9a;
  }
  html, body {
    margin: 0;
    padding: 0;
    width: 852px;
    height: 1200px;
    overflow: hidden;
    background: var(--paper);
  }
  .letterhead {
    position: relative;
    width: 852px;
    height: 1200px;
    box-sizing: border-box;
    border: 1px solid var(--edge);
    background: var(--paper);
    overflow: hidden;
    font-family: "Arimo", Arial, sans-serif;
  }
  .leaf-backdrop {
    position: absolute;
    right: 0;
    bottom: 0;
    width: 500px;
    height: 1200px;
    background: radial-gradient(ellipse 75% 62% at 72% 58%, var(--leaf-tone) 0%, rgba(236,236,236,0.6) 55%, rgba(255,255,255,0) 100%);
  }
  .brand {
    position: absolute;
    left: 62px;
    top: 112px;
    display: flex;
    align-items: center;
    gap: 10px;
    color: var(--orange);
    font-size: 19px;
    font-weight: 400;
    letter-spacing: 3px;
    text-transform: uppercase;
  }
  .brand-dot {
    width: 10px;
    height: 10px;
    border-radius: 50%;
    background: var(--orange);
  }
  .sender {
    position: absolute;
    left: 55px;
    top: 1096px;
  }
  .sender-name {
    margin: 0;
    color: var(--orange);
    font-size: 23px;
    font-weight: 700;
    line-height: 27px;
  }
  .sender-title {
    margin: 0;
    color: var(--grey-text);
    font-size: 23px;
    font-weight: 700;
    line-height: 27px;
  }
  .sender-address {
    margin: 3px 0 0 1px;
    color: var(--grey-light);
    font-style: normal;
    font-size: 9.5px;
    letter-spacing: 1px;
    line-height: 13px;
  }
  .sender-web {
    color: var(--orange);
  }
</style>
</head>
<body>
  <div class="letterhead">
    <div class="leaf-backdrop" role="img" aria-label="Faint grey leaf illustration spreading across the right side"></div>

    <div class="brand">
      <span class="brand-dot"></span>
      <span class="brand-name">Dorian Welk</span>
    </div>

    <footer class="sender">
      <p class="sender-name">DORIAN WELK</p>
      <p class="sender-title">NATUROPATH</p>
      <address class="sender-address">
        Shop 4123c, 46 Carrow Lane,<br>
        Sydney 2000 <span class="sender-web">dorianwelk.com.au</span>
      </address>
    </footer>
  </div>
</body>
</html>
```